Website for 9 year old artist, helps animal rescue charity :)

I am looking to have a simple website created for my 9 year old son's small "company." He makes necklaces and art out of beachcombed treasures and sells them for animal rescue charity. Currently, his domain name www.gullcovepebblecraft.com brings people straight to his chatterly page, but for those who are not on CH, nothing shows up.

I would like a simple landing page + a few other clickable pages that will show his logo (already done by Pixel Guild folks!) +
* photos
* a brief description about what he does
* a link to the charities he supports
* link to his Chatterly Page (https://www.chatterly.com/GullCovePebblecraft)
* are where a link to a possible wovly store could go (future, we haven't gotten that far). :)
(really just a "shop" button)
I need to be able to add and remove photos and text, add calendar dates of events he will be at, and adjust links if needed.

I hope this isn't too complicated! It doesn't need to be flashy, just an easy on the eyes page where people who are interested in his necklaces and his charity work can go to find out more. I would like to have the website incorporate the two logos (see uploads). I image the image of the child beachcombing being on the bottom anchoring the page, but that is as far as my imagination has gone regarding the web design! :)

UPDATED:
Name of web url: www.gullcovepebblecraft.com
Name of company: Gull Cove Pebblecraft
Purpose: Owen is 9 years old. He beachcombs with his family all over the United States and finds wonderful shells, seaglass, and pottery. His mom helps him drill the holes in these piece and then he creates one of a kind necklaces using these beachcombed treasures and silver charms. He also makes sweet shell, seaglass and driftwood angels (Owen's Seraphs). All shells are responsibly collected. Every piece is designed by Owen.

At least 20% off all proceeds from every sale goes to animal rescue charity.

Target Market(s)

The target market for his necklaces is typically women, but we have a lot of guys buy them, too, to hang in their windows or to give away. All ages of folks buy his necklaces at the small sales and fairs we have gone to. They also look at his site to find out more about Willow Lane Feline Shelter, the organization Owen donates a lot of his proceeds to.

We get a lot of requests about whether he has a webpage and find that many of the people who want to check it out do not have Chatterly, so linking right to CH hasn't worked.

Industry/Entity Type

Charity

Requirements
Must have
• * Logos (I have 2 done by design works folks). The one of the beachcombing child is for the website only, the one of the shell angel will be for the website and business cards, etc.
* Spaces for photos
* Clickable links to Chatterly, Wovly (later), charity(s) he donates to
* Space for Bio/backstory
* Contact us area

Match the blues of the two logos so they are the same shade.

The look should be young and simple, without being childish. We are beachcombers at heart, so sea and sand colors would work great. All blues (except electric), greens, tans, etc are great.

I added a ton of images for reference. Please message me if you would like more.
Nice to have
• * Area I can add the tally of how much he has donated so far
* Slideshow of images (I uploaded a ton for examples)
* Page dedicated to images and information about the of the rescue organization he primarily donates to. The rescue organization is dedicated to the rehabilitation and adoption of special needs and abused cats.
Should not have
• Curlz font or anything too cutesy

Bright colors, I am hoping for a more muted, seas-inspired look.

```html
<!DOCTYPE html>
<html lang="en">
<head>
<meta charset="utf-8">
<title>Willow Lane Feline Shelter · Gull Cove Pebblecraft</title>
<link href="https://fonts.googleapis.com/css2?family=Handlee&family=Ubuntu:wght@400;500&display=swap" rel="stylesheet">
<style>
:root{
  --top-bar:#3f77b1;
  --sky-top:#f6fcfe;
  --sky-low:#e3f5f9;
  --cloud:#bfe5ee;
  --cloud-deep:#a9d9e6;
  --sand-light:#fdf1e2;
  --sand:#f4c995;
  --brand:#1aa7df;
  --heading:#2d6fa8;
  --link:#2e6fae;
  --text:#3a3a3a;
  --nav-top:#fbdca8;
  --nav-bottom:#f0bf78;
  --nav-active-top:#e3c9a3;
  --nav-active-bottom:#c9a77b;
  --nav-text:#5a3b1c;
  --social:#8fb3da;
  --social-dark:#3f77b1;
  --panel-line:#bfe2ee;
  --thumb-line:#a9cfe0;
  --footer:#8cb1db;
  --footer-ink:#1d3451;
  --footer-rule:#36567d;
  --bottom-bar:#9db1c7;
  --teal:#8dcdc2;
  --grass:#8fc95a;
  --earth:#dcb987;
  --photo-warm:#9b7358;
}
*{box-sizing:border-box;margin:0;padding:0}
html,body{width:964px;height:1200px;overflow:hidden}
body{font-family:"Ubuntu",sans-serif;color:var(--text);background:var(--sky-top)}
.canvas{position:relative;width:964px;height:1200px;overflow:hidden;
  background:linear-gradient(to bottom,var(--sky-top) 0,var(--sky-low) 200px,var(--sky-low) 100%)}
.abs{position:absolute}

.top-bar{left:0;top:0;width:964px;height:4px;background:var(--top-bar)}

.cloud-band{left:0;top:215px;width:964px;height:560px;
  background:linear-gradient(to bottom,rgba(191,229,238,0) 0,var(--cloud) 60px,var(--cloud-deep) 300px,var(--cloud) 460px,rgba(191,229,238,0) 560px)}
.sand{left:0;top:735px;width:964px;height:235px;
  background:linear-gradient(to bottom,rgba(253,241,226,0) 0,var(--sand-light) 40px,#fadcb6 150px,var(--sand) 235px)}
.child{left:64px;top:772px;width:74px;height:192px;border-radius:37px 37px 18px 18px;
  background:linear-gradient(to bottom,rgba(141,205,194,.75),rgba(141,205,194,.45))}
.shore{left:150px;top:944px;width:730px;height:8px;border-radius:4px;background:var(--teal);opacity:.35}

/* brand */
.brand{left:170px;top:10px;width:120px;text-align:center}
.brand-name{font-family:"Handlee",cursive;font-size:12px;line-height:14px;color:var(--brand);display:block;white-space:nowrap}
.brand-mark{width:58px;height:58px;border-radius:50%;background:var(--brand);margin:5px auto 0}

/* social */
.social{left:653px;top:4px;display:flex;gap:2px}
.social span{width:25px;height:25px;background:var(--social);display:flex;align-items:center;justify-content:center}
.social .more{background:var(--social-dark)}

/* nav */
.main-nav{left:368px;top:47px;display:flex;gap:3px}
.main-nav a{display:block;width:62px;height:28px;border-radius:5px;text-align:center;
  font-family:"Handlee",cursive;font-size:14px;line-height:28px;color:var(--nav-text);text-decoration:none;
  background:linear-gradient(var(--nav-top),var(--nav-bottom));box-shadow:0 1px 2px rgba(120,80,30,.35)}
.main-nav a.wide{width:66px}
.main-nav a.active{background:linear-gradient(var(--nav-active-top),var(--nav-active-bottom))}

.page-title{left:175px;top:117px;font-family:"Handlee",cursive;font-size:13.5px;color:var(--brand)}
.breadcrumb{left:175px;top:137px;font-size:9.5px;color:#333}
.breadcrumb a{color:var(--link);text-decoration:none}

/* panel */
.panel{left:144px;top:157px;width:677px;height:620px;border:1px solid var(--panel-line);border-bottom:none;border-radius:8px 8px 0 0;
  background:linear-gradient(to bottom,rgba(240,250,253,.92) 0,rgba(225,244,249,.75) 420px,rgba(225,244,249,0) 620px)}

.article{left:160px;top:180px;width:466px;font-size:10.5px;line-height:14.4px}
.article h1{font-family:"Handlee",cursive;font-weight:400;font-size:15.5px;color:var(--heading);margin-bottom:12px}
.article p{margin-bottom:14.4px}
.shelter-mark{float:left;width:100px;height:86px;margin:0 32px 10px 22px;border-radius:6px;
  background:linear-gradient(135deg,#cfd6d8,#9ea7ab)}
.article-photo{float:right;width:146px;height:92px;margin:30px 0 6px 26px;border:2px solid #fff;outline:1px solid var(--thumb-line);
  background:linear-gradient(135deg,var(--photo-warm),#6d5a4c)}

/* sidebar */
.side-head{left:640px;width:150px;height:42px}
.side-head .art{position:absolute;inset:0;border-radius:0 0 20px 20px;background:linear-gradient(to bottom,var(--grass) 0,var(--grass) 50%,var(--earth) 50%)}
.side-head h2{position:absolute;left:0;right:0;text-align:center;top:16px;font-family:"Handlee",cursive;font-weight:400;font-size:14.5px;color:#fff;text-shadow:0 1px 2px rgba(90,60,20,.6)}
.video{left:648px;top:221px;width:131px;height:86px;border:2px solid #fff;outline:1px solid var(--thumb-line);background:#1c1c1c;color:#fff}
.video-title{position:absolute;left:8px;top:8px;font-size:8.5px;white-space:nowrap}
.video-frame{position:absolute;left:4px;top:24px;width:119px;height:40px;background:linear-gradient(135deg,#6c6561,#3a3432)}
.video-bar{position:absolute;left:4px;bottom:4px;width:119px;height:14px;background:#2b2b2b}

.news{left:648px;top:380px;width:150px}
.news-item{display:flex;gap:7px;height:78px;border-bottom:1px solid var(--thumb-line);padding-top:0}
.news-item+.news-item{padding-top:8px}
.news-item:last-child{border-bottom:none}
.news-thumb{flex:0 0 47px;height:47px;border:2px solid #fff;outline:1px solid var(--thumb-line)}
.news-item h3{font-family:"Handlee",cursive;font-weight:400;font-size:12px;color:var(--link);line-height:14px}
.news-item p{font-size:9.6px;line-height:13px;color:#333}

/* strip */
.strip{left:161px;top:689px;display:flex}
.strip figure{width:134px;height:88px;border:2px solid #fff;outline:1px solid var(--thumb-line)}
.strip .sep{width:31px;height:88px;position:relative}
.strip .sep::after{content:"";position:absolute;left:15px;top:0;height:88px;border-left:1px dashed #9fb7c2}

/* footer */
.footer{left:0;top:970px;width:964px;height:194px;background:var(--footer)}
.col{top:985px;width:152px}
.col h4{font-family:"Handlee",cursive;font-weight:400;font-size:18px;color:var(--footer-ink);padding-bottom:3px;border-bottom:1px dashed var(--footer-rule)}
.col ul{list-style:none;margin-top:12px}
.col li{font-size:10.5px;color:var(--footer-ink);height:23.6px;display:flex;align-items:center;gap:6px;border-bottom:1px solid rgba(255,255,255,.22)}
.col li:last-child{border-bottom:none}
.bubble{width:12px;height:8px;border-radius:50%;background:#fff}
.plugin{left:492px;top:1010px;width:152px;height:131px;background:#dbe6f2;border:1px solid #a9bdd3;padding:5px;font-size:7.5px;color:#3b5998}
.plugin-top{display:flex;gap:5px}
.plugin-icon{width:24px;height:24px;border-radius:50%;background:var(--brand);border:2px solid #fff}
.plugin-like{display:inline-block;margin-top:2px;padding:1px 4px;border:1px solid #aaa;background:#f4f4f4;color:#333}
.plugin-count{margin:6px 0 4px;color:#555;white-space:nowrap}
.faces{display:grid;grid-template-columns:repeat(5,24px);gap:3px}
.faces span{height:24px;background:#b9a08c}
.plugin-foot{margin-top:6px;color:#555}
.gallery-grid{display:grid;grid-template-columns:repeat(3,45px);gap:8px 8px;margin-top:12px}
.gallery-grid span{height:45px;border:2px solid #fff;border-radius:2px}

.bottom-bar{left:0;top:1164px;width:964px;height:36px;background:var(--bottom-bar)}
.copyright{left:151px;top:1177px;font-size:9.5px;color:#1d2d40}
</style>
</head>
<body>
<div class="canvas">
  <div class="abs top-bar"></div>
  <div class="abs cloud-band" role="img" aria-label="Soft drifting sky-blue clouds"></div>
  <div class="abs sand" role="img" aria-label="Sandy beach"></div>
  <div class="abs child" role="img" aria-label="Silhouette of a child beachcombing"></div>
  <div class="abs shore" role="img" aria-label="Row of starfish and pebbles along the shore"></div>

  <div class="abs brand">
    <span class="brand-name">Gull Cove Pebblecraft</span>
    <div class="brand-mark"></div>
  </div>

  <div class="abs social">
    <span aria-label="Search"><svg width="13" height="13" viewBox="0 0 13 13"><circle cx="5.5" cy="5.5" r="4" fill="none" stroke="#fff" stroke-width="1.8"/><line x1="8.5" y1="8.5" x2="12" y2="12" stroke="#fff" stroke-width="2"/></svg></span>
    <span aria-label="Messages"><svg width="14" height="13" viewBox="0 0 14 13"><path d="M2 1h10a1.5 1.5 0 0 1 1.5 1.5v5A1.5 1.5 0 0 1 12 9H6l-3 3V9H2A1.5 1.5 0 0 1 .5 7.5v-5A1.5 1.5 0 0 1 2 1z" fill="#fff"/></svg></span>
    <span aria-label="Videos"><svg width="14" height="12" viewBox="0 0 14 12"><rect x=".5" y=".5" width="13" height="11" rx="2.5" fill="#fff"/><path d="M5.5 3.5v5l4-2.5z" fill="var(--social)"/></svg></span>
    <span aria-label="Community page"><svg width="13" height="13" viewBox="0 0 13 13"><circle cx="6.5" cy="4" r="2.8" fill="#fff"/><path d="M1 12.5c0-3 2.5-5 5.5-5s5.5 2 5.5 5z" fill="#fff"/></svg></span>
    <span aria-label="Feed"><svg width="13" height="13" viewBox="0 0 13 13"><circle cx="2.5" cy="10.5" r="1.7" fill="#fff"/><path d="M1 6a6 6 0 0 1 6 6M1 1.5A10.5 10.5 0 0 1 11.5 12" fill="none" stroke="#fff" stroke-width="1.8"/></svg></span>
    <span class="more" aria-label="More"><svg width="13" height="13" viewBox="0 0 13 13"><path d="M6.5 1v11M1 6.5h11" stroke="#fff" stroke-width="2"/></svg></span>
  </div>

  <nav class="abs main-nav">
    <a href="#">Home</a><a href="#">About</a><a href="#">Gallery</a><a href="#">Events</a><a href="#" class="active wide">Charities</a><a href="#">Store</a><a href="#" class="wide">Contact</a>
  </nav>

  <div class="abs page-title">Willow Lane Feline Shelter</div>
  <div class="abs breadcrumb"><a href="#">Home</a> &gt; Willow Lane Feline Shelter</div>

  <div class="abs panel"></div>

  <article class="abs article">
    <h1>Willow Lane Feline Shelter</h1>
    <div class="shelter-mark" role="img" aria-label="Shelter emblem: cat silhouette with adopt-a-friend lettering"></div>
    <p>Willow Lane Feline Shelter is a non-profit effort dedicated to the rescue, rehabilitation and placement of abandoned, ill, injured and special-needs animals.</p>
    <p>All cats are tested for FeLV (leukemia) and FIV (feline infectious virus). They are spayed or neutered, vaccinated, microchipped, treated for parasites and given individual medical care as needed. They are kept separate from other cats for at least 21 days to rule out any possible virus transmission and to build trust and their sense of security. They are then integrated with others depending on disposition, age and dietary needs.</p>
    <p>Because our rescue efforts focus mainly on the ill and/or injured and special-needs cats, we are sometimes faced with the difficult decision of euthanasia. It's never easy to make this decision, but for some terminally ill or severely injured cats, particularly feral ones who are suffering, it is the kindest act that they will ever know from humans. It's a sad fact, but one that we are trying to change through community education and spay/neuter. We are committed to giving each and every cat thorough diagnostics and treatment. It is necessary to try to limit our number of rescue residents so that we can remain able to provide the time and finances needed for the often extensive medical care and rehabilitation.</p>
    <div class="article-photo" role="img" aria-label="Photo of a volunteer bottle-feeding a kitten"></div>
    <p>We relocate feral cats from unsafe areas, so we are always in need of secure homes for them such as a barn where they are fed, sheltered and monitored. All ferals are altered, vaccinated and given complete medical care, including dental treatment. We provide information on incorporating feral cats as an integral part of a healthy environment.</p>
    <p>Potential adopters are screened by application process, and an adoption donation is requested. All adoptions are lifetime guaranteed in that if the new family is ever unable to keep the cat, he/she is to be returned to Willow Lane.</p>
  </article>

  <div class="abs side-head" style="top:166px"><div class="art" role="img" aria-label="Grass and cat banner"></div><h2>Cat Rescue Video</h2></div>
  <div class="abs video">
    <div class="video-title">Cat Rescue 2012 Origina…</div>
    <div class="video-frame" role="img" aria-label="Video still of a rescued cat"></div>
    <div class="video-bar"></div>
  </div>

  <div class="abs side-head" style="top:328px"><div class="art" role="img" aria-label="Grass and cat banner"></div><h2>Latest News</h2></div>
  <div class="abs news">
    <div class="news-item"><div class="news-thumb" role="img" aria-label="Rescued cat photo" style="background:#8a6d55"></div><div><h3>Lorem ipsum</h3><p>Lorem ipsum dolor sit amet, consectetur adipisicing elit...</p></div></div>
    <div class="news-item"><div class="news-thumb" role="img" aria-label="Tabby cat photo" style="background:#a89a88"></div><div><h3>Lorem ipsum</h3><p>Lorem ipsum dolor sit amet, consectetur adipisicing elit...</p></div></div>
    <div class="news-item"><div class="news-thumb" role="img" aria-label="Kitten photo" style="background:#8f9aa2"></div><div><h3>Lorem ipsum</h3><p>Lorem ipsum dolor sit amet, consectetur adipisicing elit...</p></div></div>
    <div class="news-item"><div class="news-thumb" role="img" aria-label="Kittens photo" style="background:#b9b3ad"></div><div><h3>Lorem ipsum</h3><p>Lorem ipsum dolor sit amet, consectetur adipisicing elit...</p></div></div>
  </div>

  <div class="abs strip">
    <figure role="img" aria-label="Volunteer holding a cat" style="background:linear-gradient(135deg,#7d6a5a,#4c3f36)"></figure><div class="sep"></div>
    <figure role="img" aria-label="White cat resting" style="background:linear-gradient(135deg,#ece6df,#c9bfb5)"></figure><div class="sep"></div>
    <figure role="img" aria-label="Kitten being bottle-fed" style="background:linear-gradient(135deg,#b07a4c,#3b2c24)"></figure><div class="sep"></div>
    <figure role="img" aria-label="Vet checking a kitten" style="background:linear-gradient(135deg,#9a7a66,#5d6f86)"></figure>
  </div>

  <footer class="abs footer"></footer>

  <section class="abs col" style="left:145px">
    <h4>Latest Posts</h4>
    <ul>
      <li><span class="bubble"></span>Image Post</li>
      <li><span class="bubble"></span>Video Post</li>
      <li><span class="bubble"></span>Image Post</li>
      <li><span class="bubble"></span>Text blog post</li>
      <li><span class="bubble"></span>Video post</li>
    </ul>
  </section>

  <section class="abs col" style="left:318px">
    <h4>Archives</h4>
    <ul>
      <li><svg width="11" height="11" viewBox="0 0 11 11"><path d="M1 10l2-5 5-4 2 2-4 5z" fill="#fff"/></svg>October 2013</li>
      <li><svg width="11" height="11" viewBox="0 0 11 11"><path d="M1 10l2-5 5-4 2 2-4 5z" fill="#fff"/></svg>September 2013</li>
      <li><svg width="11" height="11" viewBox="0 0 11 11"><path d="M1 10l2-5 5-4 2 2-4 5z" fill="#fff"/></svg>August 2013</li>
      <li><svg width="11" height="11" viewBox="0 0 11 11"><path d="M1 10l2-5 5-4 2 2-4 5z" fill="#fff"/></svg>July 2013</li>
      <li><svg width="11" height="11" viewBox="0 0 11 11"><path d="M1 10l2-5 5-4 2 2-4 5z" fill="#fff"/></svg>June 2013</li>
    </ul>
  </section>

  <section class="abs col" style="left:492px">
    <h4 style="border-bottom:none">Chatterly</h4>
  </section>
  <div class="abs plugin">
    <div class="plugin-top">
      <div class="plugin-icon"></div>
      <div><div>Gull Cove Pebblecraft</div><span class="plugin-like">Like</span></div>
    </div>
    <div class="plugin-count">2,709 people like Gull Cove Pebblecraft.</div>
    <div class="faces" role="img" aria-label="Grid of follower portraits">
      <span></span><span></span><span></span><span></span><span></span>
      <span></span><span></span><span></span><span></span><span></span>
    </div>
    <div class="plugin-foot">Chatterly social plugin</div>
  </div>

  <section class="abs col" style="left:666px">
    <h4>Gallery</h4>
    <div class="gallery-grid">
      <span role="img" aria-label="Sea glass necklace" style="background:#8c9584"></span>
      <span role="img" aria-label="Beachcombing on the shore" style="background:#8a8fa0"></span>
      <span role="img" aria-label="Shell angel" style="background:#9aa894"></span>
      <span role="img" aria-label="Collected shells" style="background:#a89f92"></span>
      <span role="img" aria-label="Pottery shards" style="background:#7d7a78"></span>
      <span role="img" aria-label="Sea glass pendant" style="background:#7e9a86"></span>
    </div>
  </section>

  <div class="abs bottom-bar"></div>
  <div class="abs copyright">Copyrights@2013 : Gull Cove Pebblecraft</div>
</div>
</body>
</html>
```